Personal development products that change your life

This is a direct selling business that sells personal development courses, but also sells the business as well if desired. This is not MLM, and there is no handling of the product required, nor hassling friends or family. We are looking for business minded people wanting to work their own hours and achieve a desirable income from this. A success image or happy image on a flyer would be great. I'd like the website address to be displayed as well thanks. www.gainpath-hub.com.au

Target Market(s)

Business-minded individuals searching for more finances. Self motivated, driven, interested in self development.

Industry/Entity Type

Business

Font styles to use
Sans Serif

Requirements
Must have
• Are you looking for
• - a franchise or business?
• - a change of career?
• - a back up income?
• Not MLM
• No product handling or shipping
• No hard sales required
• website: www.gainpath-hub.com.au
Nice to have
• A picture or background of excited person jumping in the air, or some similar.
• Worded to enrol people interested in achieving more financial headway, or flexible hours, or travel and do this business from anywhere in the world.
• Only need access to a phone, internet connection and a desire to succeed.

```html
<!DOCTYPE html>
<html lang="en">
<head>
<meta charset="utf-8">
<title>Gain Path Hub flyer</title>
<link href="https://fonts.googleapis.com/css2?family=Montserrat:wght@600;700;800&family=Questrial&family=Oswald:wght@500&display=swap" rel="stylesheet">
<style>
  :root {
    --page-bg: #d9d9d9;
    --orange: #e2702a;
    --orange-deep: #c95a1b;
    --steel-light: #c4c5c7;
    --steel-mid: #8d8f92;
    --steel-dark: #57595c;
    --teal-light: #3c7680;
    --teal-dark: #1f4650;
    --white: #ffffff;
    --button-dark: #3a3a3c;
  }
  * { box-sizing: border-box; margin: 0; padding: 0; }
  html, body { width: 900px; height: 1200px; overflow: hidden; }
  body { background: var(--page-bg); position: relative; font-family: "Questrial", sans-serif; }

  .flyer {
    position: absolute; left: 52px; top: 35px; width: 798px; height: 1130px;
    overflow: hidden; background: var(--teal-dark);
    box-shadow: 0 8px 30px rgba(0,0,0,.35);
  }
  .header-band {
    position: absolute; left: 0; top: 0; width: 100%; height: 187px;
    background: linear-gradient(90deg, var(--steel-dark) 0%, var(--steel-light) 50%, var(--steel-dark) 100%);
  }
  .brand-name {
    position: absolute; left: 0; width: 100%; top: 44px; text-align: center;
    font-family: "Montserrat", sans-serif; font-weight: 800; font-size: 78px;
    color: var(--orange); letter-spacing: 1px; line-height: 1;
  }
  .tagline {
    position: absolute; left: 0; width: 100%; top: 133px; text-align: center;
    font-family: "Montserrat", sans-serif; font-weight: 700; font-size: 15.5px; color: var(--white);
  }
  .hero-photo {
    position: absolute; left: 0; top: 187px; width: 100%; height: 410px;
    background: linear-gradient(180deg, #6f7f93 0%, #a7a2a6 35%, #e29a62 70%, #c8531f 88%, #1b1512 96%, #0f0c0a 100%);
  }
  .divider-band {
    position: absolute; left: 0; top: 597px; width: 100%; height: 23px;
    background: linear-gradient(90deg, var(--steel-dark), var(--steel-light), var(--steel-dark));
  }
  .desk-photo {
    position: absolute; left: 0; top: 620px; width: 100%; height: 490px;
    background: radial-gradient(ellipse at 60% 70%, #4f8790 0%, var(--teal-light) 35%, var(--teal-dark) 100%);
  }
  .footer-band {
    position: absolute; left: 0; bottom: 0; width: 100%; height: 20px;
    background: linear-gradient(90deg, var(--steel-dark), var(--steel-light), var(--steel-dark));
  }
  .balance-badge {
    position: absolute; left: 493px; top: 478px; width: 290px; height: 290px; border-radius: 50%;
    background: rgba(200,200,200,.55); display: flex; align-items: center; justify-content: center;
  }
  .balance-badge__inner {
    width: 244px; height: 244px; border-radius: 50%; background: var(--orange);
    display: flex; align-items: center; justify-content: center; text-align: center;
    color: var(--white); font-family: "Montserrat", sans-serif; font-weight: 600; font-size: 23px; line-height: 1.45;
  }
  .question-title {
    position: absolute; left: 54px; top: 638px; color: var(--white);
    font-family: "Montserrat", sans-serif; font-weight: 600; font-size: 21px;
  }
  .checklist { position: absolute; left: 50px; top: 679px; list-style: none; }
  .checklist li {
    display: flex; align-items: center; gap: 7px; height: 32.5px;
    color: var(--white); font-size: 19px;
  }
  .requirements {
    position: absolute; left: 42px; top: 796px; display: flex; gap: 10px; align-items: flex-start;
    color: var(--white); font-family: "Montserrat", sans-serif; font-weight: 600; font-size: 15.5px; line-height: 1.45;
  }
  .requirements svg { flex: none; margin-top: 6px; }
  .benefit-tab {
    position: absolute; left: 0; height: 45px; padding-left: 70px;
    background: var(--orange); color: var(--white);
    font-family: "Montserrat", sans-serif; font-weight: 600; font-size: 23px;
    display: flex; align-items: center; border-radius: 0 3px 3px 0;
  }
  .benefit-tab::before {
    content: ""; position: absolute; left: 38px; top: 0; width: 10px; height: 45px;
    border-radius: 0 10px 10px 0; background: var(--orange-deep); opacity: .55;
  }
  .benefit-tab--mlm { top: 870px; width: 241px; }
  .benefit-tab--sales { top: 923px; width: 368px; }
  .benefit-tab--shipping { top: 976px; width: 481px; }
  .web-button {
    position: absolute; left: 258px; top: 1047px; width: 282px; height: 58px; border-radius: 10px;
    background: linear-gradient(180deg, #5a5a5d, var(--button-dark) 60%, #262628);
    box-shadow: 0 4px 8px rgba(0,0,0,.4);
    display: flex; align-items: center; justify-content: center;
    color: var(--white); font-family: "Oswald", sans-serif; font-weight: 500; font-size: 19px; letter-spacing: .3px;
  }
</style>
</head>
<body>
  <main class="flyer">
    <header class="header-band">
      <h1 class="brand-name">Gain Path Hub</h1>
      <p class="tagline">Ongoing personal development opportunities for successful applicants</p>
    </header>

    <div class="hero-photo" role="img" aria-label="Silhouettes of a group of people jumping with raised arms against a sunset sky"></div>
    <div class="divider-band"></div>
    <div class="desk-photo" role="img" aria-label="Soft teal-toned photo of hands working at a desk with a laptop"></div>
    <div class="footer-band"></div>

    <div class="balance-badge">
      <p class="balance-badge__inner">Start the work /<br>life balance<br>you've always<br>wanted</p>
    </div>

    <h2 class="question-title">Are you looking for :</h2>
    <ul class="checklist">
      <li><svg width="23" height="23" viewBox="0 0 24 24"><circle cx="12" cy="12" r="10" fill="none" stroke="#fff" stroke-width="2.4"/><path d="M7 12.5l3.2 3.2L17 8.8" fill="none" stroke="#fff" stroke-width="2.6" stroke-linecap="round" stroke-linejoin="round"/></svg>a franchise or business?</li>
      <li><svg width="23" height="23" viewBox="0 0 24 24"><circle cx="12" cy="12" r="10" fill="none" stroke="#fff" stroke-width="2.4"/><path d="M7 12.5l3.2 3.2L17 8.8" fill="none" stroke="#fff" stroke-width="2.6" stroke-linecap="round" stroke-linejoin="round"/></svg>a change of career?</li>
      <li><svg width="23" height="23" viewBox="0 0 24 24"><circle cx="12" cy="12" r="10" fill="none" stroke="#fff" stroke-width="2.4"/><path d="M7 12.5l3.2 3.2L17 8.8" fill="none" stroke="#fff" stroke-width="2.6" stroke-linecap="round" stroke-linejoin="round"/></svg>a back up income?</li>
    </ul>

    <div class="requirements">
      <svg width="40" height="40" viewBox="0 0 40 40"><circle cx="20" cy="20" r="17" fill="none" stroke="#fff" stroke-width="3"/><rect x="13" y="11" width="9" height="12" fill="#fff"/><rect x="17" y="15" width="10" height="13" fill="#fff" stroke="#1f4650" stroke-width="1.5"/></svg>
      <p>All you need is a laptop, a phone,&nbsp; internet connection, a strong desire<br>to succeed,&nbsp; and dedicate 15-20 hours per week</p>
    </div>

    <p class="benefit-tab benefit-tab--mlm">Not MLM</p>
    <p class="benefit-tab benefit-tab--sales">No hard sales required</p>
    <p class="benefit-tab benefit-tab--shipping">No product handling or shipping</p>

    <p class="web-button">WWW.GAINPATH-HUB.COM.AU</p>
  </main>
</body>
</html>
```